Brannigan Schedule Oversight Group Inc. needs a logo design (BSOGI) and a business card design

We need a logo design and business card design for a new company. Simple yet elegant/stylish and professional. to the point. Focal point BRANNIGAN...underneith Schedule Oversight Group Inc smaller font. Plus a logo that can be on the opposite side of the business card and used for T-Shirts.
Back back ground, silver/grey font. I like the look of QVR Design logo
Target Market(s)
Project controls, Planning, Scheduling, Engineering, Project Management
Industry/Entity Type
Business
Contact Information for Business Card
Company name on one side, logo and details on the other
Font styles to use
Requirements
Must have
- Rosalind Brannigan
- Project Planner
- BranniganSOGI@mailnest.example
- P.O. Box 7
- Kestrelford AB CANADA
- T0M2J3
- +1 (403) 555 0187
Nice to have
- Your input :) quote "Fail to plan, plan to fail"
Should not have
- Too much!

```html
<!DOCTYPE html>
<html lang="en">
<head>
<meta charset="utf-8">
<title>Brannigan Schedule Oversight Group Inc. — Business Card</title>
<link rel="stylesheet" href="https://fonts.googleapis.com/css2?family=Open+Sans:wght@400;700&display=swap">
<style>
  :root {
    --backdrop: #e9e7e5;
    --card-blue: #2f78b9;
    --card-white: #ffffff;
    --text-light: #ffffff;
    --brand-blue: #2f78b9;
    --card-shadow: rgba(0, 0, 0, 0.18);
  }
  * { box-sizing: border-box; margin: 0; padding: 0; }
  html, body {
    width: 1200px;
    height: 900px;
    overflow: hidden;
    background: var(--backdrop);
    font-family: "Open Sans", Arial, sans-serif;
  }
  .stage { position: relative; width: 1200px; height: 900px; }

  .card {
    position: absolute;
    overflow: hidden;
    box-shadow: 0 6px 18px var(--card-shadow);
  }

  /* Front: contact side */
  .card-front {
    left: 238px; top: 62px;
    width: 555px; height: 343px;
    background: var(--card-blue);
    color: var(--text-light);
  }
  .card-front .sweep {
    position: absolute; left: 0; top: 0;
    width: 555px; height: 343px;
  }
  .contact {
    position: absolute;
    right: 30px;
    text-align: right;
  }
  .contact-name { top: 41px; }
  .person-name { font-size: 18px; font-weight: 700; line-height: 24px; }
  .person-role { font-size: 14px; line-height: 20px; }
  .contact-address { top: 180px; font-size: 14px; line-height: 20px; font-style: normal; }
  .contact-lines { top: 257px; font-size: 14px; line-height: 20px; }
  .contact-line { display: flex; justify-content: flex-end; align-items: center; gap: 7px; }
  .contact-line svg { width: 12px; height: 12px; flex: none; }

  /* Back: company side */
  .card-back {
    left: 457px; top: 518px;
    width: 560px; height: 344px;
    background: var(--card-white);
  }
  .brand {
    position: absolute;
    left: 0; right: 0; top: 110px;
    text-align: center;
    color: var(--brand-blue);
    font-weight: 400;
  }
  .brand-dot {
    display: block;
    width: 46px; height: 46px;
    margin: 0 auto 30px;
    border-radius: 50%;
    background: var(--brand-blue);
  }
  .brand-name { display: block; font-size: 40px; line-height: 44px; letter-spacing: 1px; }
  .brand-sub { display: block; font-size: 13px; line-height: 18px; letter-spacing: 2.5px; }
</style>
</head>
<body>
<main class="stage">

  <section class="card card-front" aria-label="Business card, contact side">
    <svg class="sweep" viewBox="0 0 555 343" aria-hidden="true">
      <path d="M0 0 H196 C330 60 340 250 100 343 H0 Z" fill="var(--card-white)"/>
    </svg>

    <div class="contact contact-name">
      <p class="person-name">Rosalind Brannigan</p>
      <p class="person-role">Project Planner</p>
    </div>

    <address class="contact contact-address">
      <p>P.O. Box 7</p>
      <p>Kestrelford AB CANADA</p>
      <p>T0M2J3</p>
    </address>

    <div class="contact contact-lines">
      <p class="contact-line">+1 (403) 555 0187
        <svg viewBox="0 0 24 24" aria-hidden="true"><path fill="currentColor" d="M6.6 10.8a15.1 15.1 0 0 0 6.6 6.6l2.2-2.2a1 1 0 0 1 1-.25 11.4 11.4 0 0 0 3.6.57 1 1 0 0 1 1 1V20a1 1 0 0 1-1 1A17 17 0 0 1 3 4a1 1 0 0 1 1-1h3.5a1 1 0 0 1 1 1c0 1.25.2 2.45.57 3.57a1 1 0 0 1-.25 1z"/></svg>
      </p>
      <p class="contact-line">BranniganSOGI@mailnest.example
        <svg viewBox="0 0 24 24" aria-hidden="true"><path fill="currentColor" d="M2 5h20v14H2z M3.5 6.5 12 12.5l8.5-6" stroke="var(--card-blue)" stroke-width="1.5"/></svg>
      </p>
    </div>
  </section>

  <section class="card card-back" aria-label="Business card, company side">
    <div class="brand">
      <span class="brand-dot" aria-hidden="true"></span>
      <span class="brand-name">BRANNIGAN</span>
      <span class="brand-sub">Schedule Oversight Group Inc</span>
    </div>
  </section>

</main>
</body>
</html>
```